Sunporch Tidy Works half fold brochure design

I need a brochure for a new company. The name of the company is Sunporch Tidy Works. I am a Professional Organizer. I am requesting a one fold brochure 11" wide x 8.5" high (obviously once folded 5.5" wide x 8.5" high) brochure. I have been told this may need to be designed as a flyer? I have attached a VERY BASIC layout of what I think I am looking for. I have also attached the original logos in all the different formats I have. I would like to have a very light green background & the text I have in orange please make orange. PLEASE feel free to add color to my "Sunporch Tidy Works" logo's and use light/soft green & orange shades if possible (OK to go darker for BOLD purposes) The brochure DOES NOT have to stick to this layout, again just what I THINK I want :) - THANK YOU

EDIT: 01-21-15 Remove MARGARET BELDANE from all 3 places (front, bottom inside right & back) Remove just the BELDANE from the 1st line on the back. PRIVACY & ETHICS on the back, please remove "PRIVACY &", leave Ethics and the 1st line of the text under it. Please remove all of the text following the 1st sentence. THANK YOU

```html
<!DOCTYPE html>
<html lang="en">
<head>
<meta charset="utf-8">
<title>Sunporch Tidy Works – Half Fold Brochure</title>
<link href="https://fonts.googleapis.com/css2?family=Oswald:wght@400;500;600&family=Arimo:wght@400;700&display=swap" rel="stylesheet">
<style>
:root{
  --canvas:#ebe8e3;
  --paper:#ffffff;
  --mint:#eef3e1;
  --mint-deep:#dfe9c8;
  --green:#8db85a;
  --green-dark:#6d8f3a;
  --olive:#56682a;
  --orange:#f0a12e;
  --ink:#2a2420;
  --body:#1e1e1e;
}
*{box-sizing:border-box;margin:0;padding:0}
html,body{width:1200px;height:1200px;overflow:hidden;background:var(--canvas)}
body{position:relative;font-family:'Arimo',Arial,sans-serif;color:var(--body)}
.spread{position:absolute;left:32px;width:734px;background:var(--paper);border-bottom:8px solid var(--green);overflow:hidden}
.spread--outer{top:18px;height:564px}
.spread--inner{top:590px;height:570px}
.panel{position:absolute;top:0;bottom:0;width:367px;overflow:hidden}
.panel--left{left:0}
.panel--right{left:367px}
.panel__wash{position:absolute;inset:0;width:100%;height:100%}
.tagline-tab{position:absolute;top:8px;right:8px;height:34px;width:330px;background:var(--green);color:#fff;
  font-family:'Oswald',sans-serif;font-size:17px;line-height:34px;padding-left:22px;clip-path:polygon(0 0,100% 0,100% 100%,6% 100%)}
.wordmark{font-family:'Oswald',sans-serif;font-weight:500;color:var(--ink);line-height:1.02;text-align:center}
.service-line{font-family:'Oswald',sans-serif;color:var(--orange);text-align:center}
.phone{font-family:'Oswald',sans-serif;font-weight:500;color:var(--green);text-align:center}
.web{font-family:'Oswald',sans-serif;font-weight:500;color:var(--ink);text-align:center;line-height:1.15}
.place{font-family:'Oswald',sans-serif;font-weight:500;color:var(--ink);text-align:center}
.region{font-family:'Oswald',sans-serif;color:var(--olive);text-align:center}

/* back panel */
.intro{position:absolute;left:26px;top:38px;width:314px;font-size:10.2px;line-height:1.25;text-align:justify}
.intro p{margin-bottom:11px}
.back-brand{position:absolute;left:26px;top:300px;width:160px}
.back-brand .wordmark{font-size:24px;text-align:left}
.back-brand .phone{font-size:26px;text-align:left;margin-top:20px}
.back-brand .web{font-size:11.5px;text-align:left;line-height:1.2}
.back-brand .place{font-size:24px;text-align:left;margin-top:8px}
.back-brand .region{font-size:16px;text-align:left;line-height:1}
.member-badge{position:absolute;left:200px;top:340px;width:130px;height:90px;border-radius:8px;background:var(--mint-deep)}
.ethics{position:absolute;left:180px;top:474px;width:170px;text-align:center}
.ethics h4{font-size:13px;font-weight:700;letter-spacing:.5px}
.ethics p{font-size:9px;line-height:1.55;margin-top:4px}

/* front panel */
.front .wordmark{position:absolute;left:20px;right:20px;top:70px;font-size:46px}
.front .service-line{position:absolute;left:0;right:0;top:236px;font-size:25px}
.front .phone{position:absolute;left:0;right:0;top:285px;font-size:50px}
.front .web{position:absolute;left:0;right:0;top:356px;font-size:22px}
.front .place{position:absolute;left:0;right:0;top:484px;font-size:27px;line-height:1}
.front .region{position:absolute;left:0;right:0;top:516px;font-size:17px;line-height:1}

/* inside left */
.fears{position:absolute;left:24px;top:36px;width:318px;height:520px;font-size:9.4px;line-height:1.3;text-align:center}
.fears__lead{font-family:'Oswald',sans-serif;color:var(--orange);font-size:13px;line-height:1.45;text-align:left;margin-bottom:14px;letter-spacing:-.2px}
.fears__q{font-family:'Oswald',sans-serif;color:var(--green-dark);font-size:16px;margin:12px 0 6px}
.fears p{margin-bottom:4px}
.fears__end{font-family:'Oswald',sans-serif;font-weight:500;font-size:19px;line-height:1.2;color:var(--ink);position:absolute;left:0;right:0;top:450px;text-align:center}

/* inside right */
.about{position:absolute;left:28px;top:36px;width:312px;text-align:center}
.about h2{font-family:'Oswald',sans-serif;font-weight:400;color:var(--orange);font-size:25px;line-height:1.1;margin-bottom:14px}
.about p{font-size:9.2px;line-height:1.5;margin-bottom:10px}
.about .credit{color:var(--green-dark);font-weight:700}
.services{position:absolute;left:28px;top:232px;width:312px;display:grid;grid-template-columns:162px 150px;font-family:'Oswald',sans-serif}
.services h3{font-weight:400;color:var(--orange);font-size:12px;letter-spacing:.3px;margin:0 0 4px}
.services ul{list-style:none;margin-bottom:10px}
.services li{position:relative;padding-left:14px;font-family:'Arimo',sans-serif;font-size:9px;line-height:1.45;margin-bottom:2px}
.services li::before{content:"";position:absolute;left:0;top:2px;width:9px;height:9px;border-radius:50%;background:var(--orange)}
.services li::after{content:"";position:absolute;left:2.3px;top:3.5px;width:3px;height:5px;border:solid #fff;border-width:0 1.4px 1.4px 0;transform:rotate(40deg)}
.contact-call{position:absolute;left:0;right:0;top:438px;text-align:center;font-family:'Oswald',sans-serif;color:var(--ink)}
.contact-call .small{font-size:17px;line-height:1}
.contact-call .big{font-size:29px;font-weight:500;line-height:1.1}
.contact-call .num{font-size:29px;color:var(--orange);line-height:1.2}

/* stacked covers */
.stack{position:absolute;left:784px;top:150px;width:402px;height:708px}
.stack__tab{position:absolute;left:0;right:0;height:36px;background:var(--green);border-bottom:2px solid #fff;
  clip-path:polygon(0 0,100% 0,96% 100%,0 100%);color:#fff;font-family:'Oswald',sans-serif;font-size:19px;line-height:34px;padding-left:44px;overflow:hidden;white-space:nowrap}
.cover{position:absolute;left:0;right:0;top:88px;bottom:0;overflow:hidden;background:var(--paper)}
.cover .tagline-tab{top:0;right:0;width:100%;height:46px;line-height:46px;font-size:20px;clip-path:polygon(0 0,100% 0,96% 100%,0 100%);padding-left:44px}
.cover .wordmark{position:absolute;left:20px;right:20px;top:100px;font-size:48px}
.cover .service-line{position:absolute;left:0;right:0;top:262px;font-size:27px}
.cover .phone{position:absolute;left:0;right:0;top:312px;font-size:56px}
.cover .web{position:absolute;left:0;right:0;top:390px;font-size:24px}
.cover .place{position:absolute;left:0;right:0;top:520px;font-size:29px;line-height:1}
.cover .region{position:absolute;left:0;right:0;top:555px;font-size:18px;line-height:1}
</style>
</head>
<body>

<section class="spread spread--outer" aria-label="Brochure outside spread">
  <div class="panel panel--left back">
    <svg class="panel__wash" viewBox="0 0 367 564" preserveAspectRatio="none" aria-hidden="true">
      <defs><linearGradient id="washBack" x1="0" y1="0" x2="0" y2="1"><stop offset="0" stop-color="#e7efd4"/><stop offset="1" stop-color="#f7f9f0"/></linearGradient></defs>
      <rect width="367" height="564" fill="url(#washBack)"/>
      <path d="M0 250 C120 300 250 230 367 290 L367 564 L0 564Z" fill="#ffffff"/>
      <path d="M0 270 C130 320 240 250 367 305" fill="none" stroke="#dfe9c8" stroke-width="6"/>
    </svg>
    <div class="intro">
      <p>Hello! My name is Margaret Beldane. I offer simple, fun and insightful solutions to seemingly complicated clutter and organizational problems.</p>
      <p>I am here to help if you are ready to change your home and/or workspace.</p>
      <p>My experiences of working with family, friends, co-workers and clients has proven my hard working, energetic, fun and supportive attitude makes it easier for them to get things accomplished. Helping people sort through, and be rid of, the mental and physical obstacles that have kept them stuck along with participating in their enthusiasm when they see immediate improvement is rewarding for me.</p>
      <p>I welcome the opportunity to earn your confidence through ethical, reliable and dependable hard work.</p>
    </div>
    <div class="back-brand">
      <div class="wordmark">Sunporch<br>Tidy Works</div>
      <div class="phone">301-555-0148</div>
      <div class="web">info@sunporchtidyworks.com<br>www.sunporchtidyworks.com</div>
      <div class="place">Glenmoor, MD</div>
      <div class="region">Serving MD, DC &amp; VA</div>
    </div>
    <div class="member-badge" role="img" aria-label="Membership badge"></div>
    <div class="ethics">
      <h4>ETHICS:</h4>
      <p>I abide by the standards as outlined<br>in the GHO Code of Ethics.</p>
    </div>
  </div>

  <div class="panel panel--right front">
    <svg class="panel__wash" viewBox="0 0 367 564" preserveAspectRatio="none" aria-hidden="true">
      <defs><linearGradient id="washFront" x1="0" y1="0" x2="0" y2="1"><stop offset="0" stop-color="#f4f7ec"/><stop offset=".6" stop-color="#eef3e1"/><stop offset="1" stop-color="#dde8c4"/></linearGradient></defs>
      <rect width="367" height="564" fill="url(#washFront)"/>
      <path d="M0 420 C120 470 250 380 367 430 L367 564 L0 564Z" fill="#e3ecce"/>
      <path d="M0 440 C130 490 240 400 367 450" fill="none" stroke="#ffffff" stroke-width="4"/>
    </svg>
    <div class="tagline-tab">CLARITY: “The Quality or State of Being Clear”</div>
    <div class="wordmark">Sunporch<br>Tidy Works</div>
    <div class="service-line">Organizing &amp; Decluttering Services</div>
    <div class="phone">301-555-0148</div>
    <div class="web">info@sunporchtidyworks.com<br>www.sunporchtidyworks.com</div>
    <div class="place">Glenmoor, MD</div>
    <div class="region">Serving MD, DC &amp; VA</div>
  </div>
</section>

<section class="spread spread--inner" aria-label="Brochure inside spread">
  <div class="panel panel--left">
    <div class="fears">
      <div class="fears__lead">Getting organized isn’t all about everything being in its proper place. It can also require overcoming fears and anxieties such as:</div>
      <div class="fears__q">~ “How do I start?” ~</div>
      <p>You begin by getting help from a professional. No one can do everything; everyone needs a helping hand at times. (I bring my vehicle to a mechanic when it needs service, even for just a simple oil change!)</p>
      <div class="fears__q">~ “Am I going to have to get rid of ALL my things?” ~</div>
      <p>Definitely not! There is a process that will help you decide what to keep and what you would be willing to part with. (I can help you determine the practical and monetary “worth” of something. Only you can determine its personal “value”.)</p>
      <div class="fears__q">~ “I don’t have time” ~</div>
      <p>Now you will! Getting organized will actually save you time. You will know where that “thing” is, find it quickly and avoid the time it takes to run out and purchase a new “thing”. (You will have actually created more time to enjoy the lifestyle that is important to you.)</p>
      <p style="margin-top:10px">We all have anxiety about something that prevents or inhibits us from taking action toward a solution. Whether you want someone to take over the project or a helping hand (nudge) is all you really need, a professional organizer is the perfect way to get started. Getting organized is going to be a process of progress, not perfection. It will require some level of support and continued work on your part, but the rewards will far outweigh the efforts.</p>
      <div class="fears__end">TOGETHER WE CAN CONQUER<br>THE CLUTTER AND CREATE CLARITY</div>
    </div>
  </div>

  <div class="panel panel--right">
    <div class="about">
      <h2>What is a professional organizer?</h2>
      <p>“A Professional Organizer enhances the lives of clients by designing systems and processes using organizing principles and through transferring organizing skills. Professional Organizers help individuals and businesses take control of their surroundings, their time, their paper, and their systems for life.”<br><span class="credit">– Guild of Home Organizers</span></p>
      <p>Whether you are too busy, too confused, over whelmed, tired, stressed or just don’t know where to start, I offer a variety of hands on services to help you bring a sense of fun, freedom and functionality to almost any space.</p>
    </div>
    <div class="services">
      <div>
        <h3>ATTIC – TO – BASEMENT:</h3>
        <ul><li>Sorting – Purging - Organizing</li></ul>
        <h3>PAPER CONTROL:</h3>
        <ul><li>Sorting – Purging - Organizing</li><li>Household, home office &amp; home based filing systems</li></ul>
        <h3>DOWNSIZING:</h3>
        <ul><li>Sorting – purging - organizing - labeling</li><li>Packing &amp; unpacking</li></ul>
      </div>
      <div>
        <h3>REMOVAL:</h3>
        <ul><li>Light trash &amp; proper disposal</li><li>Donations &amp; light recyclables to proper locations</li><li>Shredding Service</li></ul>
        <h3>FOLLOW UP:</h3>
        <ul><li>Routine “clutter maintenance” visits</li></ul>
      </div>
    </div>
    <div class="contact-call">
      <div class="small">FOR PROJECTS NOT LISTED ABOVE,</div>
      <div class="big">PLEASE CONTACT ME.</div>
      <div class="num">301-555-0148</div>
    </div>
  </div>
</section>

<section class="stack" aria-label="Stack of brochure covers">
  <div class="stack__tab" style="top:0">CLARITY: “The Quality or State of Being Clear”</div>
  <div class="stack__tab" style="top:28px">CLARITY: “The Quality or State of Being Clear”</div>
  <div class="stack__tab" style="top:56px">CLARITY: “The Quality or State of Being Clear”</div>
  <div class="cover">
    <svg class="panel__wash" viewBox="0 0 402 620" preserveAspectRatio="none" aria-hidden="true">
      <defs><linearGradient id="washCover" x1="0" y1="0" x2="0" y2="1"><stop offset="0" stop-color="#f4f7ec"/><stop offset=".6" stop-color="#eef3e1"/><stop offset="1" stop-color="#dde8c4"/></linearGradient></defs>
      <rect width="402" height="620" fill="url(#washCover)"/>
      <path d="M0 460 C130 515 270 420 402 470 L402 620 L0 620Z" fill="#e3ecce"/>
      <path d="M0 482 C140 535 260 440 402 492" fill="none" stroke="#ffffff" stroke-width="4"/>
    </svg>
    <div class="tagline-tab">CLARITY: “The Quality or State of Being Clear”</div>
    <div class="wordmark">Sunporch<br>Tidy Works</div>
    <div class="service-line">Organizing &amp; Decluttering Services</div>
    <div class="phone">301-555-0148</div>
    <div class="web">info@sunporchtidyworks.com<br>www.sunporchtidyworks.com</div>
    <div class="place">Glenmoor, MD</div>
    <div class="region">Serving MD, DC &amp; VA</div>
  </div>
</section>

</body>
</html>
```